Make attractive Packaging label for NUT BUTTERS jars

We at Briarwood Pantry are launching our own line of NUT BUTTERS. We will be serving them in GLASS JARS ready packaged. I need attractive luxurious design for glass jar and should be designed ready to print.
I have attached glass jar pictures and measurement sheet.
My company logo has been attached. Also company details can be found on our facebook page.
product will be

ALMOND BUTTER
CASHEW BUTTER
PEANUT BUTTER
HAZELNUT BUTTER.

Industry/Entity Type

Retail

```html
<!DOCTYPE html>
<html lang="en">
<head>
<meta charset="utf-8">
<title>Briarwood Pantry – Almond Butter Jar Label</title>
<link rel="stylesheet" href="https://fonts.googleapis.com/css2?family=Open+Sans:wght@400;800&display=swap">
<style>
  :root {
    --orange: #f7820c;
    --peach: #f9c99a;
    --cream: #fdf7ea;
    --brown: #3a1d12;
    --caramel: #a8651e;
    --ink: #1b1b1b;
    --white: #ffffff;
    --green: #5dbb2f;
    --almond-light: #d9965a;
    --almond-dark: #9c5a2a;
  }
  * { margin: 0; padding: 0; box-sizing: border-box; }
  html, body { width: 1200px; height: 1000px; overflow: hidden; background: var(--white); }
  .canvas { position: relative; width: 1200px; height: 1000px; font-family: "Open Sans", sans-serif; }
  .label { position: absolute; left: 0; top: 337px; width: 1200px; height: 270px; }
  .label-band { position: absolute; inset: 0; }
  .contact { position: absolute; left: 36px; top: 38px; list-style: none; color: var(--ink); font-size: 13.5px; line-height: 17px; }
  .contact li { position: relative; padding-left: 24px; margin-bottom: 6px; }
  .contact svg { position: absolute; left: 0; top: 1px; width: 15px; height: 15px; fill: var(--ink); }
  .brand-name { position: absolute; left: 430px; top: 40px; width: 290px; color: var(--caramel); font-weight: 800; font-size: 50px; line-height: 54px; text-align: center; letter-spacing: -1px; }
  .product-name { position: absolute; left: 584px; top: 170px; color: var(--brown); font-weight: 800; font-size: 30px; line-height: 34px; }
  .product-name span { display: block; }
  .almond-art { position: absolute; left: 720px; top: 203px; width: 76px; height: 54px; border-radius: 40px 20px 40px 30px; background: radial-gradient(circle at 40% 40%, var(--almond-light), var(--almond-dark)); }
  .badges { position: absolute; left: 873px; top: 30px; display: flex; gap: 26px; }
  .badge { width: 68px; height: 68px; border-radius: 50%; border: 4px solid var(--white); box-shadow: 0 0 0 2px var(--ink); }
  .badge.gluten-free { background: var(--orange); }
  .badge.vegan, .badge.natural { background: var(--green); }
  .about { position: absolute; left: 842px; top: 160px; width: 320px; color: var(--white); font-size: 12.5px; line-height: 20px; text-align: justify; }
</style>
</head>
<body>
<main class="canvas">
  <section class="label">
    <svg class="label-band" viewBox="0 0 1200 270" width="1200" height="270" aria-hidden="true">
      <rect x="0" y="0" width="1200" height="270" fill="var(--cream)"/>
      <rect x="0" y="0" width="1200" height="17" fill="var(--orange)"/>
      <polygon points="0,228 1200,95 1200,270 0,270" fill="var(--peach)"/>
      <polygon points="0,243 1200,110 1200,270 0,270" fill="var(--orange)"/>
    </svg>

    <ul class="contact">
      <li><svg viewBox="0 0 24 24"><path d="M12 2a7 7 0 0 0-7 7c0 5 7 13 7 13s7-8 7-13a7 7 0 0 0-7-7zm0 9.5A2.5 2.5 0 1 1 12 6.5a2.5 2.5 0 0 1 0 5z"/></svg>Harbour Lane Arcade, Upper Mill<br>Street, Dublin, Ireland</li>
      <li><svg viewBox="0 0 24 24"><circle cx="12" cy="12" r="10"/><path d="M2 12h20M12 2c3 3 3 17 0 20M12 2c-3 3-3 17 0 20" stroke="var(--white)" stroke-width="1.5" fill="none"/></svg>www.briarwoodpantry.ie</li>
      <li><svg viewBox="0 0 24 24"><path d="M2 5h20v14H2z"/><path d="M2 5l10 8 10-8" stroke="var(--white)" stroke-width="1.5" fill="none"/></svg>info@briarwoodpantry.ie</li>
      <li><svg viewBox="0 0 24 24"><path d="M6.6 10.8a15 15 0 0 0 6.6 6.6l2.2-2.2a1 1 0 0 1 1-.25 11 11 0 0 0 3.6.6 1 1 0 0 1 1 1V20a1 1 0 0 1-1 1A17 17 0 0 1 3 4a1 1 0 0 1 1-1h3.5a1 1 0 0 1 1 1 11 11 0 0 0 .6 3.6 1 1 0 0 1-.25 1z"/></svg>353 87 555 0142<br>087 555 0187<br>087 555 0142</li>
    </ul>

    <h1 class="brand-name">Briarwood Pantry</h1>

    <h2 class="product-name"><span>Almond</span><span>Butter</span></h2>
    <div class="almond-art" role="img" aria-label="Illustration of whole almonds with a green leaf"></div>

    <div class="badges">
      <div class="badge gluten-free" role="img" aria-label="Gluten free badge"></div>
      <div class="badge vegan" role="img" aria-label="Vegan badge"></div>
      <div class="badge natural" role="img" aria-label="100% natural badge"></div>
    </div>

    <p class="about">A unique Dublin's only exquisite edible Nuts, Seed and Dried Fruit shop. From sweet and savoury snacking nuts to raw healthy nuts &amp; seeds and Dried fruits.</p>
  </section>
</main>
</body>
</html>
```